Natural Light/Organic/Documentary Photography Business

I like a simple, approachable, feminine, earthy/organic feel. Earth/neutral tones, nothing too loud or obnoxious. I like the watercolor look. I don't want anything too trendy or something I'll get tired of after a couple months. As far as colors, I am much more a fan of cream/taupe/blue/green...not a fan of pink or purple at all.

Target Market(s)

Weddings & Families

Industry/Entity Type

Wedding Photography

Contact Information for Business Card

website, email, phone number

Font styles to use
Other font styles liked:
• Horizontes, Gotham

Colors

Designer to choose colors to be used in the design.

Requirements
Must have
• Website: www.meliskaverholt.com
• Phone: 482.319.6047
• Email: tessa@meliskaverholt.com
Nice to have
• I like the watercolor look but its not necessary. I like simple/earthy tones. Nothing too loud or distracting. Simple & feminine without being too girly. I like an approachable/soft feel.
• Instagram: www.instagram.com/meliskaverholtphotography/
Should not have
• NO loud colors or design or pattern. I do not want a photo of a camera or lens or anything cheesy like that.

```html
<!DOCTYPE html>
<html lang="en">
<head>
<meta charset="UTF-8">
<title>Tessa Meliskaverholt Photography – Business Card</title>
<link href="https://fonts.googleapis.com/css2?family=Bebas+Neue&family=Montserrat:wght@400&display=swap" rel="stylesheet">
<style>
  :root {
    --backdrop: #f3f3f3;
    --taupe: #e8ddd6;
    --taupe-light: #efe6e0;
    --paper: #fafafa;
    --sage: #889c9b;
    --ink: #2b2f45;
    --rule: #8d8d8d;
  }
  * { margin: 0; padding: 0; box-sizing: border-box; }
  html, body {
    width: 1200px;
    height: 1200px;
    overflow: hidden;
    background: var(--backdrop);
  }
  .business-card {
    position: absolute;
    left: 100px;
    top: 275px;
    width: 1000px;
    height: 651px;
    background: var(--paper);
    box-shadow: 0 3px 8px rgba(0, 0, 0, 0.12);
    overflow: hidden;
  }
  .taupe-panel {
    position: absolute;
    left: 0;
    top: 0;
    width: 612px;
    height: 100%;
    background: var(--taupe);
  }
  .contact-details {
    position: absolute;
    left: 72px;
    top: 97px;
    width: 150px;
    height: 460px;
    writing-mode: vertical-rl;
    font-family: "Bebas Neue", "Oswald", sans-serif;
    font-size: 21px;
    line-height: 50px;
    letter-spacing: 0.24em;
    color: var(--ink);
    list-style: none;
  }
  .contact-details .contact-web { padding-top: 28px; }
  .contact-details .contact-phone { padding-top: 65px; }
  .contact-details .contact-email { padding-top: 0; }
  .ring-artwork {
    position: absolute;
    left: 312px;
    top: 262px;
    width: 300px;
    height: 389px;
    background: radial-gradient(ellipse at 55% 60%, var(--taupe-light) 0%, var(--taupe) 75%);
  }
  .wordmark {
    position: absolute;
    left: 331px;
    top: 102px;
    width: 600px;
    text-align: center;
    color: var(--ink);
  }
  .wordmark-name {
    font-family: "Bebas Neue", "Oswald", sans-serif;
    font-size: 64px;
    line-height: 1;
    letter-spacing: 0.05em;
    font-weight: 400;
  }
  .wordmark-tagline {
    margin-top: 8px;
    font-family: "Montserrat", sans-serif;
    font-size: 13px;
    letter-spacing: 0.62em;
    padding-left: 0.62em;
  }
  .wordmark-divider {
    position: absolute;
    left: 567px;
    top: 222px;
    width: 128px;
    height: 1px;
    background: var(--rule);
  }
  .social-band {
    position: absolute;
    left: 350px;
    top: 511px;
    right: 0;
    height: 66px;
    background: var(--sage);
    display: flex;
    align-items: center;
    padding-left: 28px;
    font-family: "Bebas Neue", "Oswald", sans-serif;
    font-size: 23px;
    letter-spacing: 0.2em;
    color: var(--paper);
    white-space: nowrap;
  }
</style>
</head>
<body>
  <article class="business-card">
    <div class="taupe-panel"></div>
    <div class="ring-artwork" role="img" aria-label="Line illustration of two interlocking wedding rings with a diamond, in white on taupe"></div>
    <ul class="contact-details">
      <li class="contact-web">www.meliskaverholt.com</li>
      <li class="contact-phone">Phone: 482.319.6047</li>
      <li class="contact-email">tessa@meliskaverholt.com</li>
    </ul>
    <header class="wordmark">
      <h1 class="wordmark-name">Tessa Meliskaverholt</h1>
      <p class="wordmark-tagline">PHOTOGRAPHY</p>
    </header>
    <div class="wordmark-divider"></div>
    <div class="social-band">Instagram / meliskaverholtphotography</div>
  </article>
</body>
</html>
```